Project management consultancy needs a website designed

Our company (Keystone PMO) currently has a website (http://www.keystonepmo-example.com.au) that needs to be re-designed and enhanced. Company is a professional services/consultancy business focused on project management. We are looking for something more professional. It would be advantageous if the website can be hosted in SharePoint. We are reasonably happy with the content, what we're after is something that has better aesthetics. Attached to the brief is a copy of our logo in vector format.

Target Market(s)

Small to medium businesses

Industry/Entity Type

It Company

Contact Information for Business Card

logo/company name on back, contact details plus smaller logo on front. Information to display = Name, title, address, phone number, email address, website address

Coding

Coded - Design and coding required

Number of Pages Required

4 page

Font styles to use
Sans Serif

Requirements
Must have
• Website must have: A home page, content page, contact details page (including a contact us function), blog. Project management related images/photos
Nice to have
• Website has the ability to support video content

```html
<!DOCTYPE html>
<html lang="en">
<head>
<meta charset="utf-8">
<title>Keystone PMO</title>
<link rel="stylesheet" href="https://fonts.googleapis.com/css2?family=Questrial&family=Arimo:wght@400;700&display=swap">
<style>
  :root {
    --blue: #1a78d2;
    --white: #ffffff;
    --ink: #555555;
    --body: #6a6a6a;
    --light-bg: #f4f4f4;
    --footer-bg: #232323;
    --footer-line: #3a3a3a;
    --footer-text: #9a9a9a;
    --footer-head: #e6e6e6;
    --icon: #b4b4b4;
  }
  * { margin: 0; padding: 0; box-sizing: border-box; }
  html, body { width: 1180px; height: 1200px; overflow: hidden; background: var(--white); }
  body { position: relative; font-family: "Arimo", Arial, sans-serif; color: var(--body); }

  .site-header { position: absolute; top: 0; left: 0; width: 1180px; height: 50px; background: var(--white); }
  .brand { position: absolute; left: 254px; top: 8px; display: flex; align-items: center; gap: 8px; }
  .brand-mark { width: 34px; height: 34px; background: var(--blue); border-radius: 5px; }
  .brand-name { font-family: "Questrial", sans-serif; font-size: 22px; color: var(--blue); letter-spacing: 0.5px; }
  .main-nav { position: absolute; top: 20px; right: 234px; display: flex; gap: 26px; }
  .main-nav a { font-family: "Arimo", sans-serif; font-size: 8.5px; font-weight: 700; letter-spacing: 0.6px; color: #666; text-decoration: none; text-transform: uppercase; }
  .main-nav a.active { color: var(--blue); }

  .hero { position: absolute; top: 50px; left: 0; width: 1180px; height: 334px; overflow: hidden; }
  .hero-photo { position: absolute; inset: 0;
    background:
      radial-gradient(ellipse 260px 180px at 840px 210px, rgba(70,140,200,0.55), transparent 70%),
      linear-gradient(90deg, #050505 0%, #0b0b0c 30%, #1e2228 55%, #3b4550 75%, #5a6470 100%); }
  .hero-content { position: absolute; top: 120px; left: 0; width: 100%; text-align: center; color: var(--white); }
  .hero-title { font-family: "Questrial", sans-serif; font-size: 20px; font-weight: 700; letter-spacing: 0.3px; }
  .hero-tagline { margin-top: 8px; font-size: 10.5px; font-weight: 700; }
  .play-button { display: block; margin: 13px auto 0; }

  .section-title { font-family: "Questrial", sans-serif; font-size: 16px; color: var(--ink); text-align: center; }
  .title-rule { width: 40px; height: 2px; background: var(--blue); margin: 10px auto 0; }

  .about { position: absolute; top: 384px; left: 0; width: 1180px; height: 254px; background: var(--light-bg); padding-top: 48px; }
  .about-text { width: 580px; margin: 22px auto 0; text-align: center; font-size: 8.8px; line-height: 12.8px; color: var(--body); }
  .about-text p + p { margin-top: 12.6px; }

  .benefits { position: absolute; top: 638px; left: 0; width: 1180px; height: 237px; padding-top: 44px; }
  .benefit { position: absolute; top: 92px; width: 160px; text-align: center; font-size: 8.8px; line-height: 12.6px; color: var(--body); }
  .benefit svg { display: block; margin: 0 auto 12px; }
  .benefit-capital { left: 296px; }
  .benefit-focus { left: 520px; }
  .benefit-delivery { left: 752px; }

  .site-footer { position: absolute; top: 875px; left: 0; width: 1180px; height: 325px; background: var(--footer-bg); }
  .footer-tagline { position: absolute; top: 28px; width: 100%; text-align: center; font-family: "Questrial", sans-serif; font-size: 16px; color: var(--white); }
  .footer-link { position: absolute; top: 53px; width: 100%; text-align: center; font-size: 10px; color: var(--blue); }
  .footer-rule { position: absolute; left: 254px; width: 692px; height: 1px; background: var(--footer-line); }
  .footer-rule.top { top: 87px; }
  .footer-rule.bottom { top: 272px; }
  .footer-col { position: absolute; top: 118px; }
  .footer-col h3 { font-size: 9.6px; font-weight: 700; letter-spacing: 0.8px; color: var(--footer-head); text-transform: uppercase; }
  .footer-col ul { list-style: none; margin-top: 24px; }
  .footer-col li { font-size: 8.6px; color: var(--footer-text); height: 17.3px; }
  .col-links { left: 254px; }
  .col-contact { left: 412px; }
  .col-connect { left: 590px; width: 140px; }
  .col-blogs { left: 781px; }
  .col-contact p { margin-top: 24px; font-size: 8.6px; color: var(--footer-text); }
  .connect-intro { margin-top: 25px; font-size: 6.8px; line-height: 9.6px; color: var(--footer-text); }
  .social { display: flex; align-items: center; gap: 10px; margin-top: 8px; font-size: 8.6px; color: var(--footer-text); }
  .social-dot { width: 16px; height: 16px; border-radius: 50%; background: var(--blue); }
  .col-blogs li { height: 20.7px; }
  .copyright { position: absolute; top: 294px; width: 100%; text-align: center; font-size: 8.4px; font-weight: 700; color: #777; letter-spacing: 0.3px; }
</style>
</head>
<body>

<header class="site-header">
  <div class="brand">
    <span class="brand-mark"></span>
    <span class="brand-name">Keystone PMO</span>
  </div>
  <nav class="main-nav">
    <a class="active" href="#">Home</a>
    <a href="#">Who We Are</a>
    <a href="#">What We Do</a>
    <a href="#">Why Choose Us</a>
    <a href="#">Blogs</a>
    <a href="#">Contact Us</a>
  </nav>
</header>

<section class="hero">
  <div class="hero-photo" role="img" aria-label="Businessman's hand holding a globe surrounded by a tablet, laptop, phone and connected network nodes, dark blue tones"></div>
  <div class="hero-content">
    <h1 class="hero-title">Keystone Portfolio Management Office</h1>
    <p class="hero-tagline">Offering you a competitive alternative to traditional in-house PMOs</p>
    <svg class="play-button" width="40" height="40" viewBox="0 0 40 40" aria-label="Play video">
      <circle cx="20" cy="20" r="18.5" fill="none" stroke="#ffffff" stroke-width="1.4"/>
      <path d="M17 14 L26 20 L17 26 Z" fill="#ffffff"/>
    </svg>
  </div>
</section>

<section class="about">
  <h2 class="section-title">About Company Profile</h2>
  <div class="title-rule"></div>
  <div class="about-text">
    <p>Our team of professionals comes equipped with a wealth of experience in both the private and public sectors. Let our professionally certified experts monitor and improve your project management so that you can focus on your business.</p>
    <p>We aim to align the selection and execution of projects and programs with your organization's business goals, thereby increasing the success of project execution. We provide coordination, guidance, and training to your project teams, coaching them in your company's methodologies and standards for each project.</p>
    <p>Most importantly, we work with you to implement these strategies in a way that works with your individual organization and fits your specific needs.<br>We provide the tools, knowledge and experience so that you will have confidence in the overall management of your projects and get back to concentrating on your business.</p>
  </div>
</section>

<section class="benefits">
  <h2 class="section-title">Keystone PMO will allow you to</h2>
  <div class="title-rule"></div>

  <div class="benefit benefit-capital">
    <svg width="44" height="40" viewBox="0 0 44 40" aria-hidden="true">
      <g fill="none" stroke="var(--icon)" stroke-width="3">
        <circle cx="16" cy="22" r="8"/>
        <circle cx="33" cy="12" r="5"/>
        <circle cx="33" cy="31" r="4.5"/>
      </g>
      <g stroke="var(--icon)" stroke-width="4" stroke-linecap="butt">
        <path d="M16 9v5M16 30v5M3 22h5M24 22h5M6.8 12.8l3.5 3.5M21.7 27.7l3.5 3.5M6.8 31.2l3.5-3.5M21.7 16.3l3.5-3.5"/>
        <path d="M33 3v3M33 18v3M24 12h3M39 12h3"/>
        <path d="M33 23.5v2.5M33 36v2.5M25.5 31h2.5M38 31h2.5"/>
      </g>
    </svg>
    Optimize the use of your capital. We'll help you avoid project inefficiency and maximize success by choosing the right projects the first time, every time.
  </div>

  <div class="benefit benefit-focus">
    <svg width="42" height="42" viewBox="0 0 42 42" aria-hidden="true">
      <circle cx="21" cy="21" r="18.5" fill="none" stroke="var(--icon)" stroke-width="3"/>
      <circle cx="21" cy="21" r="14" fill="none" stroke="var(--icon)" stroke-width="1"/>
      <path d="M21 10v11h8" fill="none" stroke="var(--icon)" stroke-width="2.4" stroke-linecap="round"/>
    </svg>
    Filter out the noise; you have enough on your plate without being inundated with data. We'll communicate efficiently to provide you with the important information you need.
  </div>

  <div class="benefit benefit-delivery">
    <svg width="42" height="42" viewBox="0 0 42 42" aria-hidden="true">
      <path d="M6 36 L26 16" stroke="var(--icon)" stroke-width="5" stroke-linecap="round"/>
      <path d="M26 16 a8 8 0 1 1 6 -12 l-5 5 l2 4 l4 2 l5 -5 a8 8 0 0 1 -12 6" fill="var(--icon)"/>
      <path d="M8 6 L36 34" stroke="var(--icon)" stroke-width="4" stroke-linecap="round"/>
      <rect x="3" y="3" width="8" height="8" rx="1.5" fill="var(--icon)" transform="rotate(45 7 7)"/>
    </svg>
    Let Project Managers focus on what they know best – project outcomes. They won't have be burdened with administration.
  </div>
</section>

<footer class="site-footer">
  <p class="footer-tagline">You know your business, we know PMOs.</p>
  <p class="footer-link">What's the advantage</p>
  <div class="footer-rule top"></div>

  <div class="footer-col col-links">
    <h3>Site Link</h3>
    <ul>
      <li>Home</li>
      <li>About Us</li>
      <li>Who We Are</li>
      <li>What We do</li>
      <li>Why Choose Us</li>
      <li>Why Keystone PMO</li>
    </ul>
  </div>

  <div class="footer-col col-contact">
    <h3>Contact</h3>
    <p>enquiries@keystonepmo-example.com.au</p>
  </div>

  <div class="footer-col col-connect">
    <h3>Connect</h3>
    <p class="connect-intro">Lorem ipsum dolor sit amet, consectetur adipisicing elit, sed do eiusmod tempor incididunt ut labore et dolore magna aliqua.</p>
    <div class="social"><span class="social-dot"></span>Find on Linkup</div>
    <div class="social"><span class="social-dot"></span>Get In Touch</div>
  </div>

  <div class="footer-col col-blogs">
    <h3>Recent Blogs</h3>
    <ul>
      <li>Lorem ipsum dolor sit amet</li>
      <li>Consectetur adipisicing elit sed do eiusmod</li>
      <li>Tempor incididunt ut</li>
      <li>Ut enim ad minim veniam quis nostrud</li>
      <li>Exercitation ullamco laboris nisi ut aliquip</li>
    </ul>
  </div>

  <div class="footer-rule bottom"></div>
  <p class="copyright">Copyright © 2015 KEYSTONE PMO</p>
</footer>

</body>
</html>
```